Summer Drinks Flyer for Coffee Shop

We are a coffee shop in London and would like to have a cool and nice flyer for our summer drinks (juices and frozen drink) flyer - see on the attached file for the list

Attached you can find an "attempt" - please note that I would no necessary need the image below.

I also attache our new logo.

thank you

Industry/Entity Type

Coffee Shop

```html
<!DOCTYPE html>
<html lang="en">
<head>
<meta charset="utf-8">
<title>Summer Drinks – Harbour Cup</title>
<link rel="stylesheet" href="https://fonts.googleapis.com/css2?family=Kalam:wght@700&family=Arimo:wght@400;700&family=Archivo+Black&display=swap">
<style>
  :root {
    --page-bg: #ffffff;
    --frame: #000000;
    --ink: #111111;
    --mint: #99ffc2;
    --lime: #b9fb5e;
    --caramel: #d89a56;
    --sun: #f7a21b;
    --sun-edge: #6b3e08;
  }
  * { margin: 0; padding: 0; box-sizing: border-box; }
  html, body {
    width: 1200px; height: 900px; overflow: hidden;
    background: var(--page-bg);
  }
  .flyer {
    position: absolute; left: 277px; top: 0;
    width: 647px; height: 900px;
    border: 1px solid var(--frame);
    background: var(--page-bg);
    color: var(--ink);
    font-family: "Arimo", Arial, sans-serif;
  }
  .band { position: absolute; left: 1px; width: 644px; }
  .band--frozen { top: 20px; height: 141px; background: var(--mint); }
  .band--juice { top: 184px; height: 286px; background: var(--lime); }
  .band--coffee { top: 493px; height: 225px; background: var(--caramel); }

  .band__title, .band__price {
    position: absolute;
    font-family: "Kalam", "Comic Sans MS", cursive;
    font-weight: 700;
    font-size: 38px;
    letter-spacing: 1px;
    line-height: 1;
  }
  .band__title { left: 54px; top: 17px; }
  .band__price { left: 478px; top: 17px; }

  .menu-list { position: absolute; list-style: none; font-size: 23.5px; line-height: 28.6px; }
  .band--frozen .menu-list { left: 77px; top: 66px; }
  .band--juice .menu-list { left: 80px; top: 77px; }
  .band--coffee .menu-list { left: 87px; top: 73px; }

  .extra { position: absolute; font-size: 23.5px; }
  .extra b { font-size: 28px; font-weight: 700; margin-right: 4px; vertical-align: -2px; }
  .band--juice .extra { left: 148px; top: 241px; }
  .band--coffee .extra { left: 148px; top: 177px; }

  .season-title {
    position: absolute; left: 44px; top: 756px;
    font-family: "Archivo Black", "Arial Black", sans-serif;
    font-size: 57px; line-height: 60px;
    color: var(--sun);
    -webkit-text-stroke: 2px #ffffff;
    text-shadow:
      2px 0 0 var(--sun-edge), -2px 0 0 var(--sun-edge),
      0 2px 0 var(--sun-edge), 0 -2px 0 var(--sun-edge),
      2px 2px 0 var(--sun-edge), -2px -2px 0 var(--sun-edge),
      2px -2px 0 var(--sun-edge), -2px 2px 0 var(--sun-edge);
    letter-spacing: 0.5px;
  }
  .season-title span { display: block; }
  .season-title span + span { margin-left: 22px; }

  .brand {
    position: absolute; left: 384px; top: 790px;
    width: 226px; text-align: center;
    font-family: "Arimo", Arial, sans-serif;
    font-weight: 700; font-size: 38px; line-height: 1;
    color: var(--ink);
  }
</style>
</head>
<body>
  <main class="flyer">
    <section class="band band--frozen">
      <h2 class="band__title">Frozen Fruit Drinks</h2>
      <p class="band__price">£2.95</p>
      <ul class="menu-list">
        <li>Strawberry and Banana</li>
        <li>Pineapple, Mango and Banana</li>
      </ul>
    </section>

    <section class="band band--juice">
      <h2 class="band__title">Fruit Juices</h2>
      <p class="band__price">£2.95</p>
      <ul class="menu-list">
        <li>Orange and Carrot</li>
        <li>Orange and Pineapple</li>
        <li>Pineapple and Apple</li>
        <li>Apple and Kiwi</li>
        <li>Carrot and Ginger</li>
      </ul>
      <p class="extra"><b>+</b>Add Mint or Ginger for Free!</p>
    </section>

    <section class="band band--coffee">
      <h2 class="band__title">Iced-Coffees</h2>
      <p class="band__price">£2.45</p>
      <ul class="menu-list">
        <li>Iced Coffee</li>
        <li>Iced Latte</li>
        <li>Iced Chocolate Drink</li>
      </ul>
      <p class="extra"><b>+</b>Add Syrup Shot for 10p</p>
    </section>

    <h1 class="season-title"><span>SUMMER</span><span>DRINKS</span></h1>

    <p class="brand">Harbour Cup</p>
  </main>
</body>
</html>
```